Corvale Mechanical - Letterhead

We are a plumbing and hvac company based in Calgary. This letterhead will be on our quotes, invoices, preventative maintenance proposals etc.

```html
<!DOCTYPE html>
<html lang="en">
<head>
<meta charset="utf-8">
<title>Corvale Mechanical – Letterhead</title>
<link href="https://fonts.googleapis.com/css2?family=Arimo:wght@400&family=Nunito+Sans:wght@400;600;800&display=swap" rel="stylesheet">
<style>
  :root {
    --board: #6e6e6e;
    --board-light: #a4a4a4;
    --paper: #ffffff;
    --paper-shade: #ebebeb;
    --paper-plain: #f2f2f2;
    --ink: #4a4a4a;
    --ink-soft: #555555;
    --brand-blue: #1c6fbf;
    --brand-orange: #f15a24;
    --mark-faint: #f1e3df;
    --signature-area: #ececec;
    --label: #ffffff;
  }
  * { margin: 0; padding: 0; box-sizing: border-box; }
  html, body { width: 1200px; height: 774px; overflow: hidden; }
  body {
    position: relative;
    background: linear-gradient(90deg, var(--board) 0%, var(--board) 62%, var(--board-light) 100%);
    font-family: "Arimo", Arial, sans-serif;
  }
  .page {
    position: absolute;
    top: 61px;
    width: 458px;
    height: 643px;
    box-shadow: 0 2px 4px rgba(0,0,0,0.25);
    overflow: hidden;
  }
  .page--letter {
    left: 125px;
    background: linear-gradient(160deg, var(--paper) 0%, var(--paper) 45%, var(--paper-shade) 100%);
  }
  .page--continuation {
    left: 628px;
    background: var(--paper-plain);
  }
  .faint-mark {
    position: absolute;
    border-radius: 50%;
    background: var(--mark-faint);
    opacity: 0.75;
  }
  .page--letter .faint-mark { left: 110px; top: 205px; width: 230px; height: 230px; }
  .page--continuation .faint-mark { left: 110px; top: 205px; width: 230px; height: 230px; }

  .brand {
    position: absolute;
    top: 100px;
    left: 0;
    width: 100%;
    display: flex;
    justify-content: center;
    align-items: center;
    gap: 8px;
  }
  .brand__dot {
    width: 14px; height: 14px; border-radius: 50%;
    background: var(--brand-orange);
  }
  .brand__name {
    font-family: "Nunito Sans", Arial, sans-serif;
    font-weight: 800;
    font-size: 20px;
    color: var(--brand-blue);
    letter-spacing: 0.2px;
  }

  .letter {
    position: absolute;
    left: 40px;
    top: 185px;
    width: 380px;
    color: var(--ink);
  }
  .letter__greeting { font-size: 12px; margin-bottom: 22px; color: var(--ink-soft); }
  .letter__body p {
    font-size: 7.1px;
    line-height: 9.8px;
    text-align: justify;
    margin-bottom: 9.8px;
  }
  .letter__closing { font-size: 7.1px; margin-top: 16px; }
  .letter__signature {
    display: block;
    width: 137px;
    height: 34px;
    margin-top: 2px;
    margin-left: -3px;
    background: var(--signature-area);
    border-radius: 3px;
  }

  .footer {
    position: absolute;
    left: 0;
    top: 583px;
    width: 100%;
    text-align: center;
    font-family: "Nunito Sans", Arial, sans-serif;
    font-size: 7px;
    line-height: 9px;
    color: var(--ink-soft);
  }
  .footer__name { color: var(--brand-blue); font-weight: 600; }
  .footer__rule {
    width: 210px;
    height: 0;
    border-top: 0.6px solid var(--brand-blue);
    margin: 3px auto 4px;
  }

  .page-label {
    position: absolute;
    top: 716px;
    width: 200px;
    text-align: center;
    font-family: "Nunito Sans", Arial, sans-serif;
    font-weight: 600;
    font-size: 17px;
    color: var(--label);
  }
  .page-label--first { left: 257px; }
  .page-label--second { left: 756px; }
</style>
</head>
<body>
  <section class="page page--letter">
    <div class="faint-mark" aria-hidden="true"></div>

    <header class="brand">
      <span class="brand__dot" aria-hidden="true"></span>
      <span class="brand__name">Corvale Mechanical Inc</span>
    </header>

    <article class="letter">
      <p class="letter__greeting">Dear Mr. Hartley,</p>
      <div class="letter__body">
        <p>Lorem ipsum dolor sit amet, consectetur adipiscing elit. Donec orci purus, luctus vitae dignissim eu, iaculis sed purus. Vivamus faucibus, ipsum nec aliquet viverra, leo mauris condimentum ligula, sit amet sagittis enim ligula quis arcu. Nam egestas tortor id nisi porttitor mattis. In tortor ante, ultricies in suscipit a, tempus non massa. Vivamus et auctor mi. Fusce vel massa nulla. Phasellus nec eros mauris, et scelerisque orci.</p>
        <p>Donec malesuada orci vitae nulla accumsan porta a id massa. Quisque accumsan iaculis magna sit amet fringilla. Maecenas consequat, magna eget tincidunt semper, odio nibh rutrum mi, id feugiat ante nisi eu risus. Vestibulum nunc orci, rhoncus a placerat in, ultricies in mi. Cras mattis varius eros, vel fringilla nisi suscipit eget. Quisque scelerisque sagittis nulla at porttitor.</p>
        <p>Sed id augue vitae urna euismod commodo aliquet a quam. Pellentesque arcu velit, cursus et malesuada ut, consequat et diam. Nullam erat sem, rhoncus id ullamcorper vitae, rhoncus et arcu. In ultricies ultricies nulla, ut rutrum nisi iaculis at. Donec eu magna a metus ornare faucibus. Fusce aliquet faucibus ultricies. Morbi semper, est id tincidunt gravida, sem arcu adipiscing lacus, ac bibendum nulla leo eu purus. Quisque nec diam sed risus consectetur a ccumsan quis quis nibh. Vestibulum id purus lorem.</p>
        <p>It is a long established fact that a reader will be distracted by the readable content of a page when looking at its layout. The point of using Lorem Ipsum is that it has a more-or-less normal distribution of letters, as opposed to using 'Content here, content here', making it look like readable English. Many desktop publishing packages</p>
        <p>ada ut, consequat et diam. Nullam erat sem, rhoncus id ullamcorper vitae, rhoncus et arcu. In ultricies ultricies nulla, ut rutrum nisi iaculis at. Donec eu magna a metus ornare faucibus. Fusce aliquet faucibus ultricies. Morbi semper,</p>
      </div>
      <p class="letter__closing">Sincerely,</p>
      <span class="letter__signature" role="img" aria-label="Handwritten signature of the sender"></span>
    </article>

    <footer class="footer">
      <div class="footer__name">Corvale Mechanical Inc</div>
      <div class="footer__address">2140 Larkspur Avenue SW, Calgary, Alberta T2T 4K8</div>
      <div class="footer__rule"></div>
      <div class="footer__contact">403-555-0148 | 403-555-0192 | info@corvalemechanical.com</div>
      <div class="footer__web">www.corvalemechanical.com</div>
    </footer>
  </section>

  <section class="page page--continuation">
    <div class="faint-mark" aria-hidden="true"></div>
  </section>

  <p class="page-label page-label--first">Page_01</p>
  <p class="page-label page-label--second">Page_02</p>
</body>
</html>
```